business card design for heron textile printing

Heron Textile Printing requires elegant and colorful designs for its business card, ensuring both are visually cohesive and reflect the brand’s creative, modern identity. The logo is already finalized and should be a central element in designs.

## Business Card Design Brief

- Feature the logo clearly, with colors and style matching the letterhead.
- Present contact information (name, title, phone, email, website, address) in a clear, organized manner.
- Open to creative layouts, finishes, and double-sided designs, as long as the card remains professional and easy to read.
- Ensure both pieces feel unified as part of the same brand identity.

The final designs should be vibrant, professional, and memorable, showcasing Heron Textile Printing’s creative spirit.

Target Market(s)

Pakistan

Industry/Entity Type

Textile printing

Other font styles liked:
• Calibri

Requirements
Must have
• Address Email Address Phone number designer can ask me when start designing

```html
<!DOCTYPE html>
<html lang="en">
<head>
<meta charset="utf-8">
<title>Heron Textile Printing — Business Card</title>
<link href="https://fonts.googleapis.com/css2?family=Poppins:wght@400;500;600;700&display=swap" rel="stylesheet">
<style>
  :root {
    --stage: #2b2e33;
    --card-front: #ffffff;
    --card-back: #0f0f10;
    --maroon: #5b1a20;
    --maroon-soft: #8a2f2a;
    --ink: #2a2a2a;
    --orange: #f26a21;
    --purple: #7a3fc4;
    --magenta: #d62f8f;
  }
  * { box-sizing: border-box; margin: 0; padding: 0; }
  html, body {
    width: 1200px; height: 900px; overflow: hidden;
    background: var(--stage);
    font-family: "Poppins", sans-serif;
  }
  .stage {
    width: 1200px; height: 900px;
    display: flex; align-items: center; justify-content: center; gap: 80px;
  }
  .card {
    width: 360px; height: 620px;
    border-radius: 26px;
    position: relative;
    overflow: hidden;
    box-shadow: 0 18px 40px rgba(0,0,0,.35);
  }
  .card--front { background: var(--card-front); }
  .card--back { background: var(--card-back); }

  .brand {
    position: absolute; left: 0; right: 0;
    display: flex; flex-direction: column; align-items: center; gap: 18px;
  }
  .card--front .brand { top: 70px; }
  .card--back .brand { top: 150px; }
  .brand-mark {
    width: 170px; height: 170px; border-radius: 50%;
    background: linear-gradient(160deg, var(--purple) 0%, var(--magenta) 48%, var(--orange) 100%);
  }
  .brand-name {
    font-weight: 600; font-size: 24px; letter-spacing: 1px;
    text-align: center; line-height: 1.2;
  }
  .card--front .brand-name { color: var(--maroon); }
  .card--back .brand-name { color: var(--maroon-soft); }

  .person {
    position: absolute; left: 48px; top: 360px;
  }
  .person-name { font-weight: 700; font-size: 22px; color: var(--maroon); }
  .person-title { font-size: 13px; color: var(--ink); }

  .address {
    position: absolute; left: 48px; top: 430px;
    font-size: 13px; color: var(--ink); line-height: 1.5;
  }
  .contact {
    position: absolute; left: 48px; top: 490px;
    list-style: none; font-size: 13px; color: var(--ink);
    display: flex; flex-direction: column; gap: 7px;
  }
  .contact li { display: flex; align-items: center; gap: 10px; }
  .contact svg { width: 14px; height: 14px; flex: none; }
</style>
</head>
<body>
<main class="stage">
  <section class="card card--front" aria-label="Business card front">
    <div class="brand">
      <div class="brand-mark"></div>
      <div class="brand-name">Heron Textile Printing</div>
    </div>
    <div class="person">
      <div class="person-name">Daniel Reyes</div>
      <div class="person-title">CEO &amp; Founder</div>
    </div>
    <div class="address">418 Linden Mill Lane<br>Suite #207</div>
    <ul class="contact">
      <li>
        <svg viewBox="0 0 24 24" fill="var(--orange)"><path d="M6.6 10.8a15 15 0 0 0 6.6 6.6l2.2-2.2a1 1 0 0 1 1-.25 11.4 11.4 0 0 0 3.6.57 1 1 0 0 1 1 1V20a1 1 0 0 1-1 1A17 17 0 0 1 3 4a1 1 0 0 1 1-1h3.5a1 1 0 0 1 1 1c0 1.25.2 2.45.57 3.57a1 1 0 0 1-.25 1z"/></svg>
        (555) 014-2286
      </li>
      <li>
        <svg viewBox="0 0 24 24" fill="var(--orange)"><path d="M2 5h20v14H2z" /><path d="M2 5l10 8 10-8" fill="none" stroke="#fff" stroke-width="2"/></svg>
        info@herontextileprinting.com
      </li>
      <li>
        <svg viewBox="0 0 24 24" fill="none" stroke="var(--orange)" stroke-width="2"><circle cx="12" cy="12" r="9"/><path d="M3 12h18M12 3a14 14 0 0 1 0 18M12 3a14 14 0 0 0 0 18"/></svg>
        www.herontextileprinting.com
      </li>
    </ul>
  </section>

  <section class="card card--back" aria-label="Business card back">
    <div class="brand">
      <div class="brand-mark"></div>
      <div class="brand-name">Heron Textile Printing</div>
    </div>
  </section>
</main>
</body>
</html>
```